Business Reporting Graph Illustration

I'm looking for a graphic design to created an illustration of a line chart I have two sample charts that I'd like elements of each combined together to create the project. Below is a link to learn more about this project. This should be designed using any product of the Adobe Suite.
Color Scheme is included within the below link. This will require 2 - 3 rounds of design before final completion.

https://www.plonvadesk.com/file/QWT8HbxuLeMRa302KD5Vpt/Graphic-Design-Project

```html
<!DOCTYPE html>
<html lang="en">
<head>
<meta charset="utf-8">
<title>Direct Response Attribution Chart</title>
<link rel="stylesheet" href="https://fonts.googleapis.com/css2?family=Source+Sans+3:wght@600;700&display=swap">
<style>
  :root {
    --ink: #1d2744;
    --line-blue: #5a7db6;
    --axis-blue: #5b80bd;
    --tag-blue: #4f7bbd;
    --accent-orange: #f6a623;
    --paper: #ffffff;
  }
  html, body {
    margin: 0;
    padding: 0;
    width: 1200px;
    height: 315px;
    overflow: hidden;
    background: var(--paper);
  }
  .chart {
    display: block;
    width: 1200px;
    height: 315px;
    font-family: "Source Sans 3", "Myriad Pro", sans-serif;
  }
  .label { fill: var(--ink); font-weight: 700; }
  .label--small { font-size: 15px; }
  .label--note { font-size: 21px; }
  .axis-number { fill: var(--axis-blue); font-weight: 700; font-size: 19px; text-anchor: middle; }
  .axis-line, .axis-tick { stroke: var(--axis-blue); stroke-width: 3; fill: none; }
  .response-curve { stroke: var(--line-blue); stroke-width: 2.6; fill: none; stroke-linejoin: round; }
  .marker-line { stroke: var(--accent-orange); stroke-width: 2.6; fill: none; }
  .marker-head, .spot-flag { fill: var(--accent-orange); }
  .window-line { stroke: var(--accent-orange); stroke-width: 2.6; stroke-dasharray: 8 8; fill: none; }
  .ad-tag { fill: var(--tag-blue); }
  .ad-tag-text { fill: var(--paper); font-weight: 700; font-size: 15px; text-anchor: middle; }
  .window-arrow { stroke: var(--axis-blue); stroke-width: 2.4; fill: none; }
  .window-arrow-head { fill: var(--axis-blue); }
</style>
</head>
<body>
<svg class="chart" viewBox="0 0 2560 672" role="img" aria-label="Line chart of direct response over twenty minutes, showing lifts after TV spots and attribution windows around TV ads">

  <!-- attribution windows -->
  <g class="ad-windows">
    <line class="window-line" x1="1474" y1="75" x2="1474" y2="603"/>
    <line class="window-line" x1="1535" y1="75" x2="1535" y2="603"/>
    <line class="window-line" x1="1908" y1="75" x2="1908" y2="603"/>
    <line class="window-line" x1="1969" y1="75" x2="1969" y2="603"/>
    <line class="window-line" x1="2206" y1="75" x2="2206" y2="603"/>
    <line class="window-line" x1="2267" y1="75" x2="2267" y2="603"/>

    <rect class="ad-tag" x="1437" y="118" width="78" height="26"/>
    <text class="ad-tag-text" x="1476" y="136">TV Ad</text>
    <rect class="ad-tag" x="1870" y="118" width="78" height="26"/>
    <text class="ad-tag-text" x="1909" y="136">TV Ad</text>
    <rect class="ad-tag" x="2163" y="118" width="78" height="26"/>
    <text class="ad-tag-text" x="2202" y="136">TV Ad</text>

    <text class="label label--small" x="1852" y="188" text-anchor="middle">Attribution</text>
    <text class="label label--small" x="1852" y="207" text-anchor="middle">window</text>
    <line class="window-arrow" x1="1922" y1="191" x2="1958" y2="191"/>
    <polygon class="window-arrow-head" points="1914,191 1924,185 1924,197"/>
    <polygon class="window-arrow-head" points="1966,191 1956,185 1956,197"/>
  </g>

  <!-- axis -->
  <g class="axis">
    <line class="axis-line" x1="112" y1="603" x2="2533" y2="603"/>
    <g class="axis-ticks">
      <line class="axis-tick" x1="400" y1="590" x2="400" y2="615"/>
      <line class="axis-tick" x1="512" y1="590" x2="512" y2="615"/>
      <line class="axis-tick" x1="625" y1="590" x2="625" y2="615"/>
      <line class="axis-tick" x1="737" y1="590" x2="737" y2="615"/>
      <line class="axis-tick" x1="849" y1="590" x2="849" y2="615"/>
      <line class="axis-tick" x1="962" y1="590" x2="962" y2="615"/>
      <line class="axis-tick" x1="1074" y1="590" x2="1074" y2="615"/>
      <line class="axis-tick" x1="1186" y1="590" x2="1186" y2="615"/>
      <line class="axis-tick" x1="1298" y1="590" x2="1298" y2="615"/>
      <line class="axis-tick" x1="1410" y1="590" x2="1410" y2="615"/>
      <line class="axis-tick" x1="1522" y1="590" x2="1522" y2="615"/>
      <line class="axis-tick" x1="1635" y1="590" x2="1635" y2="615"/>
      <line class="axis-tick" x1="1747" y1="590" x2="1747" y2="615"/>
      <line class="axis-tick" x1="1860" y1="590" x2="1860" y2="615"/>
      <line class="axis-tick" x1="1972" y1="590" x2="1972" y2="615"/>
      <line class="axis-tick" x1="2084" y1="590" x2="2084" y2="615"/>
      <line class="axis-tick" x1="2196" y1="590" x2="2196" y2="615"/>
      <line class="axis-tick" x1="2309" y1="590" x2="2309" y2="615"/>
      <line class="axis-tick" x1="2421" y1="590" x2="2421" y2="615"/>
      <line class="axis-tick" x1="2533" y1="590" x2="2533" y2="615"/>
    </g>
    <g class="axis-numbers">
      <text class="axis-number" x="341" y="642">1</text>
      <text class="axis-number" x="453" y="642">2</text>
      <text class="axis-number" x="566" y="642">3</text>
      <text class="axis-number" x="678" y="642">4</text>
      <text class="axis-number" x="791" y="642">5</text>
      <text class="axis-number" x="903" y="642">6</text>
      <text class="axis-number" x="1016" y="642">7</text>
      <text class="axis-number" x="1128" y="642">8</text>
      <text class="axis-number" x="1241" y="642">9</text>
      <text class="axis-number" x="1357" y="642">10</text>
      <text class="axis-number" x="1469" y="642">11</text>
      <text class="axis-number" x="1582" y="642">12</text>
      <text class="axis-number" x="1694" y="642">13</text>
      <text class="axis-number" x="1807" y="642">14</text>
      <text class="axis-number" x="1919" y="642">15</text>
      <text class="axis-number" x="2032" y="642">16</text>
      <text class="axis-number" x="2144" y="642">17</text>
      <text class="axis-number" x="2257" y="642">18</text>
      <text class="axis-number" x="2369" y="642">19</text>
      <text class="axis-number" x="2481" y="642">20</text>
    </g>
    <text class="label label--small" x="42" y="610">MINUTES</text>
  </g>

  <!-- response curve -->
  <path class="response-curve" d="
    M116,578 C130,590 140,600 150,608 C160,614 180,616 205,600 C225,588 245,582 270,590 C285,595 300,600 318,592
    C330,570 325,520 330,500 C336,470 344,440 350,415 C352,380 348,318 368,317 C386,318 385,345 387,415
    C392,440 410,430 420,428 C432,430 426,465 440,465 C455,467 465,455 478,465 C490,478 500,512 515,513
    C535,515 540,510 548,530 C558,560 565,568 580,566 C595,563 598,565 603,595 C608,605 620,595 630,588
    C650,578 680,588 710,597 C735,600 740,585 765,582 C800,580 830,595 849,598
    C860,598 872,595 882,560 C887,540 882,520 887,495 C893,470 901,440 907,415 C909,380 905,318 925,317
    C943,318 942,345 944,415 C949,440 967,430 977,428 C989,430 983,465 997,465 C1012,467 1022,455 1035,465
    C1047,478 1057,512 1072,513 C1092,515 1097,510 1105,530 C1115,560 1122,568 1137,566 C1152,563 1155,565 1160,595
    C1165,605 1175,585 1200,580 C1230,576 1260,597 1280,594 C1300,590 1330,570 1360,562 C1390,554 1420,562 1435,566
    C1455,566 1480,518 1503,520 C1520,525 1535,545 1550,555 C1570,570 1595,570 1605,558 C1615,540 1625,540 1640,550
    C1655,560 1660,560 1667,548 C1675,530 1680,510 1688,511 C1696,512 1700,545 1712,548 C1725,550 1740,535 1752,536
    C1765,537 1785,555 1800,556 C1812,555 1815,543 1830,545 C1845,547 1860,558 1880,557 C1895,556 1905,540 1908,500
    C1912,430 1914,272 1920,272 C1926,274 1930,400 1935,460 C1940,510 1945,515 1955,530 C1962,540 1965,548 1972,545
    C1978,530 1982,520 1990,521 C2005,523 2010,552 2018,555 C2025,557 2030,550 2038,555 C2043,560 2045,565 2050,555
    C2058,540 2065,535 2075,540 C2085,548 2095,545 2110,541 C2125,536 2135,540 2145,545 C2160,550 2175,550 2190,540
    C2200,530 2203,510 2205,460 C2208,300 2212,198 2218,198 C2225,200 2235,330 2245,440 C2250,500 2253,525 2260,527
    C2270,528 2280,520 2290,528 C2300,534 2305,522 2315,530 C2325,540 2335,560 2343,555 C2350,545 2360,525 2370,525
    C2385,528 2400,545 2412,545 C2420,544 2422,533 2435,538 C2445,540 2448,498 2455,498 C2462,500 2465,540 2475,535
    C2480,520 2482,497 2488,498 C2495,500 2500,535 2515,536 C2525,537 2530,534 2533,534"/>

  <!-- markers -->
  <g class="markers">
    <line class="marker-line" x1="111" y1="558" x2="111" y2="386"/>
    <polygon class="marker-head" points="111,375 105,387 117,387"/>
    <text class="label label--small" x="45" y="358">DIRECT RESPONSE</text>

    <polygon class="spot-flag" points="280,195 308,210 280,225"/>
    <text class="label label--small" x="294" y="253" text-anchor="middle">TV SPOT</text>
    <line class="marker-line" x1="292" y1="650" x2="292" y2="282"/>
    <polygon class="marker-head" points="292,271 286,283 298,283"/>

    <polygon class="spot-flag" points="836,195 864,210 836,225"/>
    <text class="label label--small" x="848" y="253" text-anchor="middle">TV SPOT</text>
    <line class="marker-line" x1="849" y1="650" x2="849" y2="282"/>
    <polygon class="marker-head" points="849,271 843,283 855,283"/>

    <line class="marker-line" x1="453" y1="255" x2="453" y2="428"/>
    <polygon class="marker-head" points="453,439 447,427 459,427"/>
    <line class="marker-line" x1="1010" y1="255" x2="1010" y2="428"/>
    <polygon class="marker-head" points="1010,439 1004,427 1016,427"/>
  </g>

  <!-- notes -->
  <g class="notes">
    <text class="label label--note" x="475" y="277">
      <tspan x="475">DIRECT RESPONSE</tspan>
      <tspan x="475" dy="26">Baseline+lift Easy yet so difficult</tspan>
      <tspan x="475" dy="26">e.g. organic growth, dual feeds,</tspan>
      <tspan x="475" dy="26">close proximity airings, etc.</tspan>
    </text>
    <text class="label label--note" x="1032" y="277">
      <tspan x="1032">DIRECT RESPONSE</tspan>
      <tspan x="1032" dy="26">Baseline+lift Easy yet so difficult</tspan>
      <tspan x="1032" dy="26">e.g. organic growth, dual feeds,</tspan>
      <tspan x="1032" dy="26">close proximity airings, etc.</tspan>
    </text>
  </g>
</svg>
</body>
</html>
```